Healthy Supplement featuring Moringa products

Need 3 business card options for our reps to order from Cardloom. Our reps will be ordering from Cardloom once we upload them. Attached is our current designs to show what info needs to be on the cards. Our website is www.tkvitality.com
The business cards will be a template for our reps to order from. Most of our reps are Asian & Hispanic. Please look at our website so you can see who we are to get the look and feel what we need.
Target Market(s)
Adults 30 on up. Health oriented people.
Industry/Entity Type
Health And Wellness
Contact Information for Business Card
Name
Title
Phone
Logo
www.tkvitality.com/my/username
Font styles to use
Requirements
Must have
- Please match our website look and colors. A moringa leaf is nice, but am open to something different.
Nice to have
- Healthy looking and warm, not super cold or too modern.
Should not have
- No harsh colors please.

```html
<!DOCTYPE html>
<html lang="en">
<head>
<meta charset="utf-8">
<title>TK Vitality Business Card</title>
<link href="https://fonts.googleapis.com/css2?family=Open+Sans:wght@400;600;800&display=swap" rel="stylesheet">
<style>
  :root {
    --backdrop: #3b3d40;
    --leaf-green: #6aaa45;
    --lime: #8dc63f;
    --paper: #ffffff;
    --ink-light: #ffffff;
    --ink-green: #6aaa45;
  }
  * { box-sizing: border-box; margin: 0; padding: 0; }
  html, body {
    width: 1200px; height: 900px; overflow: hidden;
    background: var(--backdrop);
    font-family: "Open Sans", Arial, sans-serif;
  }
  .canvas {
    position: relative; width: 1200px; height: 900px;
    display: flex; flex-direction: column; align-items: center; justify-content: center;
    gap: 56px;
  }
  .card {
    position: relative; width: 600px; height: 343px;
    border-radius: 26px; overflow: hidden;
    background: var(--leaf-green);
    box-shadow: 0 10px 24px rgba(0,0,0,.35);
  }
  .card-shapes { position: absolute; inset: 0; width: 100%; height: 100%; }
  .leaf-pattern {
    position: absolute; border-radius: 50%;
    background: radial-gradient(ellipse at center, rgba(255,255,255,.16), rgba(255,255,255,.04) 70%, rgba(255,255,255,0) 100%);
  }
  .front .leaf-pattern { top: -40px; right: 40px; width: 240px; height: 200px; }
  .back .leaf-pattern { top: 40px; right: -30px; width: 360px; height: 260px; }

  .contact { position: absolute; left: 38px; top: 44px; color: var(--ink-light); }
  .contact .name { font-weight: 800; font-size: 24px; letter-spacing: .2px; }
  .contact .title { font-size: 19px; margin: 2px 0 10px 18px; }
  .contact .location { font-size: 11.5px; line-height: 1.3; margin-left: 32px; }
  .contact .lines { list-style: none; margin: 12px 0 0 32px; }
  .contact .lines li { display: flex; align-items: center; gap: 10px; font-size: 13px; line-height: 1.6; }
  .contact .lines svg { width: 11px; height: 11px; flex: none; }

  .wordmark {
    position: absolute; font-weight: 600; letter-spacing: 2px;
    display: flex; align-items: center; gap: 10px;
  }
  .wordmark .dot { border-radius: 50%; flex: none; }
  .front .wordmark { right: 36px; top: 150px; font-size: 28px; color: var(--ink-green); }
  .front .wordmark .dot { width: 16px; height: 16px; background: var(--ink-green); }
  .back .wordmark {
    left: 50%; top: 50%; transform: translate(-50%, -50%);
    font-size: 46px; color: var(--ink-light);
  }
  .back .wordmark .dot { width: 24px; height: 24px; background: var(--ink-light); }
</style>
</head>
<body>
<main class="canvas">

  <section class="card front">
    <div class="leaf-pattern" role="img" aria-label="Faint moringa leaf branch pattern"></div>
    <svg class="card-shapes" viewBox="0 0 600 343" aria-hidden="true">
      <path d="M100 343 C 205 210, 362 92, 600 38" fill="none" stroke="var(--paper)" stroke-width="2"/>
      <path d="M112 343 C 215 215, 370 100, 600 48 L600 60 C 380 112, 232 222, 134 343 Z" fill="var(--lime)"/>
      <path d="M134 343 C 232 222, 380 112, 600 60 L600 343 Z" fill="var(--paper)"/>
    </svg>

    <div class="contact">
      <p class="name">Dana Reyes</p>
      <p class="title">Manager</p>
      <p class="location">Location<br>Cedar Grove, California</p>
      <ul class="lines">
        <li>
          <svg viewBox="0 0 12 12"><path d="M2.5 1 L4.5 1 L5.3 3.4 L4 4.3 C4.6 5.7 6.3 7.4 7.7 8 L8.6 6.7 L11 7.5 L11 9.5 C11 10.3 10.3 11 9.5 11 C5 11 1 7 1 2.5 C1 1.7 1.7 1 2.5 1 Z" fill="var(--ink-light)"/></svg>
          <span>+1(555) 204-3187</span>
        </li>
        <li>
          <svg viewBox="0 0 12 12"><rect x="1" y="2.5" width="10" height="7" fill="var(--ink-light)"/><path d="M1 2.5 L6 6.5 L11 2.5" fill="none" stroke="var(--leaf-green)" stroke-width="1"/></svg>
          <span>info@tkvitality.com</span>
        </li>
        <li>
          <svg viewBox="0 0 12 12"><circle cx="6" cy="6" r="5" fill="var(--ink-light)"/><path d="M1 6 H11 M6 1 C3.5 3.5 3.5 8.5 6 11 M6 1 C8.5 3.5 8.5 8.5 6 11" fill="none" stroke="var(--leaf-green)" stroke-width=".8"/></svg>
          <span>www.tkvitality.com</span>
        </li>
      </ul>
    </div>

    <div class="wordmark"><span class="dot"></span><span>TK VITALITY</span></div>
  </section>

  <section class="card back">
    <div class="leaf-pattern" role="img" aria-label="Faint moringa leaf branch pattern"></div>
    <div class="wordmark"><span class="dot"></span><span>TK VITALITY</span></div>
  </section>

</main>
</body>
</html>
```